We need a design for business cards for our new company. We are a resident safety and security company company that focuses on senior living communities. we provide Nurse call, Access control, CCTV, Wired and wireless network infrastructure, Wander Management, and much more!

Our logo is the circuit board shield. Representing our high tech security solutions. I would like the business card to bring the same theme with perhaps some circuit board traces around the card similar to our logo

```html
<!DOCTYPE html>
<html lang="en">
<head>
<meta charset="utf-8">
<title>ElderNova Business Cards</title>
<link href="https://fonts.googleapis.com/css2?family=Montserrat:wght@400;500;600;700&family=Oswald:wght@500&display=swap" rel="stylesheet">
<style>
  :root {
    --bg: #3a3a3c;
    --white: #ffffff;
    --ink: #1c1c1e;
    --blue: #0a8fe6;
    --blue-deep: #0a5fd6;
    --blue-light: #12a9f0;
    --black-card: #1c1c1c;
  }
  * { margin: 0; padding: 0; box-sizing: border-box; }
  html, body { width: 1200px; height: 1200px; overflow: hidden; background: var(--bg); }
  .canvas { position: relative; width: 1200px; height: 1200px; }
  .card {
    position: absolute; left: 120px; width: 960px; height: 540px;
    border-radius: 40px; overflow: hidden;
  }
  .card-front { top: 40px; background: var(--white); border-bottom: 4px solid var(--blue); }
  .card-back { top: 620px; background: var(--black-card); border-bottom: 4px solid var(--blue); }

  .holder { position: absolute; left: 70px; top: 150px; font-family: "Montserrat", sans-serif; }
  .holder-name { color: var(--blue); font-weight: 700; font-size: 34px; letter-spacing: 1px; line-height: 1; }
  .holder-title { color: var(--ink); font-weight: 500; font-size: 20px; margin-top: 4px; letter-spacing: 1px; }
  .contact-list { list-style: none; margin-top: 22px; margin-left: 40px; }
  .contact-list li { display: flex; align-items: center; gap: 12px; font-size: 25px; color: var(--ink); height: 38px; font-weight: 500; }
  .contact-list svg { width: 28px; height: 28px; flex: none; }

  .brand { position: absolute; font-family: "Montserrat", sans-serif; font-weight: 700; color: var(--blue-deep); display: flex; align-items: center; gap: 16px; }
  .brand-dot { border-radius: 50%; background: var(--blue-deep); flex: none; }
  .brand-front { right: 90px; top: 120px; font-size: 54px; }
  .brand-front .brand-dot { width: 34px; height: 34px; }
  .brand-back { left: 0; right: 0; top: 230px; justify-content: center; font-size: 72px; color: var(--blue); }
  .brand-back .brand-dot { width: 44px; height: 44px; background: var(--blue); }

  .services-heading { position: absolute; left: 470px; top: 322px; font-family: "Montserrat", sans-serif; font-weight: 600; color: var(--blue); font-size: 26px; }
  .services-band { position: absolute; left: 0; bottom: 0; width: 960px; height: 200px; }
  .services { position: absolute; left: 0; right: 0; bottom: 38px; height: 100px; font-family: "Oswald", sans-serif; color: var(--white); font-size: 18px; text-transform: uppercase; }
  .services ul { position: absolute; list-style: none; line-height: 26px; }
  .services li::before { content: "•"; margin-right: 10px; }
  .services .col-1 { left: 80px; bottom: 6px; }
  .services .col-2 { left: 400px; bottom: 22px; }
  .services .col-3 { left: 740px; bottom: 46px; }
</style>
</head>
<body>
<main class="canvas">
  <section class="card card-front">
    <div class="brand brand-front"><span class="brand-dot"></span>ElderNova</div>

    <div class="holder">
      <h1 class="holder-name">MARK HOLLOWAY</h1>
      <p class="holder-title">President</p>
      <ul class="contact-list">
        <li><svg viewBox="0 0 24 24"><path fill="#0a8fe6" d="M6.6 10.8a15 15 0 0 0 6.6 6.6l2.2-2.2c.3-.3.7-.4 1-.2 1.1.4 2.3.6 3.6.6.6 0 1 .4 1 1V20c0 .6-.4 1-1 1A17 17 0 0 1 3 4c0-.6.4-1 1-1h3.5c.6 0 1 .4 1 1 0 1.3.2 2.5.6 3.6.1.3 0 .7-.2 1z"/></svg>(555) 014-2290</li>
        <li><svg viewBox="0 0 24 24"><rect x="6" y="2" width="12" height="20" rx="2" fill="none" stroke="#0a8fe6" stroke-width="2"/><circle cx="12" cy="18.5" r="1.2" fill="#0a8fe6"/></svg>(555) 013-7781</li>
        <li><svg viewBox="0 0 24 24"><rect x="2" y="5" width="20" height="14" fill="#0a8fe6"/><path d="M2 5l10 8 10-8M2 19l8-7M22 19l-8-7" fill="none" stroke="#fff" stroke-width="1.5"/></svg>Mark@ElderNova.com</li>
        <li><svg viewBox="0 0 24 24"><circle cx="12" cy="12" r="10" fill="none" stroke="#0a8fe6" stroke-width="2"/><path d="M2 12h20M12 2c3 3 3 17 0 20M12 2c-3 3-3 17 0 20M4 7h16M4 17h16" fill="none" stroke="#0a8fe6" stroke-width="1.5"/></svg>www.ElderNova.com</li>
      </ul>
    </div>

    <h2 class="services-heading">Services</h2>
    <svg class="services-band" viewBox="0 0 960 200" preserveAspectRatio="none" aria-hidden="true">
      <defs>
        <linearGradient id="bandFill" x1="0" x2="1" y1="0" y2="0">
          <stop offset="0" stop-color="#12a9f0"/>
          <stop offset="1" stop-color="#0a5fd6"/>
        </linearGradient>
      </defs>
      <polygon points="0,110 960,20 960,150 0,175" fill="url(#bandFill)"/>
    </svg>
    <div class="services">
      <ul class="col-1"><li>Nurse Call Systems</li><li>Access Control</li></ul>
      <ul class="col-2"><li>CCTV (Closed-Circuit Television)</li><li>Wired and Wireless Network Infrastructure</li></ul>
      <ul class="col-3"><li>Wander Management</li><li>And Much More!</li></ul>
    </div>
  </section>

  <section class="card card-back">
    <div class="brand brand-back"><span class="brand-dot"></span>ElderNova</div>
  </section>
</main>
</body>
</html>
```